Hotel Business Card Project

Amber Crest Hotel will be a premium boutique hotel in Dhaka, Bangladesh. The hotel will offer the finest amenities and facilities available on the market, and the cost per room investment will far exceed other 5-star hotels currently in the market.

As a result, we wanted the business card to reflect that premium/luxurious/upscale feel, and also be elegant and hospitable at the same time.

The name 'Amber Crest' is derived from the fact that Bangladesh has 6 distinct seasons (you can get more information online if required, or contact me about it). The leaves in the logo has the tree because trees give people shade, protection and safety (just like our hotel would try to give).

Target Market(s)

Business professionals, guests

Industry/Entity Type

Investment

Requirements
Must have
• Elegant, Classy and very attractive business card.

Must be editable to enter specific Names, Positions, Phone numbers and email later on.
Nice to have
• The address would be: House 42, Road 57, Banani 4, Dhaka 1230, Bangladesh

Slogan- Luxury Redefined

```html
<!DOCTYPE html>
<html lang="en">
<head>
<meta charset="utf-8">
<title>Amber Crest Hotel — Business Card</title>
<link rel="stylesheet" href="https://fonts.googleapis.com/css2?family=Source+Sans+3:ital,wght@0,400;0,600;0,700;1,400&family=Pinyon+Script&display=swap">
<style>
  :root {
    --card-bg: #ffffff;
    --leaf-green: #e4ec99;
    --ink: #231f20;
    --ink-soft: #58595b;
    --rule: #7a7a7a;
    --amber: #d9a45b;
  }
  html, body {
    margin: 0;
    padding: 0;
    width: 1200px;
    height: 672px;
    overflow: hidden;
    background: var(--card-bg);
  }
  .card {
    position: relative;
    width: 1200px;
    height: 672px;
    background: var(--card-bg);
    overflow: hidden;
    font-family: "Source Sans 3", "Myriad Pro", Arial, sans-serif;
    color: var(--ink);
  }
  .card__backdrop {
    position: absolute;
    inset: 0;
    width: 1200px;
    height: 672px;
  }
  .card__backdrop .leaf { fill: var(--leaf-green); }

  .brand {
    position: absolute;
    left: 98px;
    top: 60px;
    width: 320px;
    text-align: center;
  }
  .brand__mark {
    display: block;
    width: 130px;
    height: 130px;
    margin: 0 auto 46px;
    border-radius: 50%;
    background: var(--amber);
  }
  .brand__name {
    margin: 0;
    font-size: 33px;
    font-weight: 400;
    letter-spacing: 1px;
    text-transform: uppercase;
    color: var(--ink-soft);
    line-height: 1;
  }

  .slogan {
    position: absolute;
    left: 543px;
    top: 36px;
    margin: 0;
    font-family: "Pinyon Script", cursive;
    font-weight: 400;
    font-size: 67px;
    line-height: 1;
    color: var(--ink-soft);
  }

  .contact {
    position: absolute;
    left: 534px;
    top: 262px;
    width: 626px;
  }
  .contact__name {
    margin: 0;
    font-size: 50px;
    font-weight: 600;
    line-height: 54px;
  }
  .contact__position {
    margin: 0;
    font-size: 40px;
    font-style: italic;
    line-height: 46px;
  }
  .contact__rule {
    height: 0;
    margin: 8px 0 14px -2px;
    border: 0;
    border-top: 2px solid var(--rule);
  }
  .contact__details,
  .contact__address {
    margin: 0;
    font-size: 40px;
    line-height: 46.5px;
  }
  .contact__address { margin-top: 16px; line-height: 44px; }
</style>
</head>
<body>
<main class="card">
  <svg class="card__backdrop" viewBox="0 0 1200 672" aria-hidden="true">
    <path class="leaf leaf--top" d="M490,0 C525,160 760,275 1200,275 L1200,0 Z"/>
    <path class="leaf leaf--bottom" d="M0,305 C205,330 352,480 380,672 L0,672 Z"/>
  </svg>

  <div class="brand">
    <span class="brand__mark"></span>
    <p class="brand__name">Amber Crest Hotel</p>
  </div>

  <p class="slogan">Luxury Redefined</p>

  <section class="contact">
    <h1 class="contact__name">Your Name</h1>
    <p class="contact__position">Position</p>
    <hr class="contact__rule">
    <p class="contact__details">
      Contact no.: 02 555 0142<br>
      Mobile: +880 1555 000142<br>
      Email: name@ambercrest.com
    </p>
    <p class="contact__address">
      House 42, Road 57, Banani 4<br>
      Dhaka 1230, Bangladesh
    </p>
  </section>
</main>
</body>
</html>
```